Bedrock Yield Private Holdings Scheme

I want a professional design for a new investment program that we have designed for prospecting new prospects. We have a company logo and the content that we would like for the brochure but we would like and design structure and graphics to help compliment the content. I am attaching a rough draft of the brochure that has some

Target Market(s)

Anyone looking for hard assets, inflation hedge, cash flow investments.

```html
<!DOCTYPE html>
<html lang="en">
<head>
<meta charset="utf-8">
<title>How the Bedrock Yield Private Holdings Scheme Works</title>
<link rel="stylesheet" href="https://fonts.googleapis.com/css2?family=Montserrat:wght@600;700;800;900&family=EB+Garamond:wght@400&display=swap">
<style>
  :root {
    --page-bg: #f1f5ec;
    --map-tone: #e2eadb;
    --heading-green: #2a5f35;
    --frame-green: #45a23c;
    --ring-dark: #17693a;
    --accent-green: #3aa336;
    --text-grey: #555b58;
    --title-grey: #565b5c;
    --band-green: #355e3c;
    --white: #ffffff;
  }
  * { box-sizing: border-box; margin: 0; padding: 0; }
  html, body { width: 848px; height: 1200px; overflow: hidden; }
  body { background: var(--page-bg); font-family: "EB Garamond", Georgia, serif; color: var(--text-grey); }
  .page { position: relative; width: 848px; height: 1200px; overflow: hidden; }

  .section-title {
    position: absolute; left: 61px; top: 72px;
    font-family: "Montserrat", Arial, sans-serif; font-weight: 700;
    font-size: 17.5px; line-height: 22px; letter-spacing: 0.6px;
    color: var(--heading-green); text-transform: uppercase;
  }
  .section-title .num { display: inline-block; width: 25px; }
  .section-title .line2 { padding-left: 25px; display: block; }

  .world-map {
    position: absolute; left: 62px; top: 380px; width: 724px; height: 400px;
    background: radial-gradient(ellipse at 50% 45%, var(--map-tone) 0%, rgba(226,234,219,0.6) 55%, rgba(241,245,236,0) 75%);
  }

  .diagram { position: absolute; left: 0; top: 0; width: 848px; height: 1200px; }

  .step-box {
    position: absolute; background: var(--white);
    border: 2.5px solid var(--frame-green); border-radius: 11px;
    padding: 16px 18px 12px 19px;
  }
  .step-box h2 {
    font-family: "Montserrat", Arial, sans-serif; font-weight: 700;
    font-size: 16px; color: var(--title-grey); margin-bottom: 3px; letter-spacing: 0.2px;
  }
  .step-box p, .step-box li { font-size: 14px; line-height: 21.3px; }
  .step-box ul { list-style: none; }
  .step-box li { position: relative; padding-left: 14px; }
  .step-box li::before { content: "•"; position: absolute; left: 0; top: 0; font-size: 11px; }

  .step-identify { left: 61px; top: 151px; width: 222px; height: 290px; }
  .step-acquire { left: 313px; top: 133px; width: 222px; height: 227px; }
  .step-reinvest { left: 565px; top: 105px; width: 223px; height: 354px; }
  .step-divest { left: 106px; top: 771px; width: 283px; height: 247px; }
  .step-manage { left: 491px; top: 771px; width: 283px; height: 290px; }

  .brand-band {
    position: absolute; left: 60px; top: 1087px; width: 729px; height: 70px;
    background: var(--band-green); color: var(--white);
    display: flex; align-items: center;
  }
  .brand-name {
    width: 106px; flex: none; text-align: center;
    font-family: "Montserrat", Arial, sans-serif; font-weight: 600;
    font-size: 8.5px; line-height: 11px; color: #c9d6c4;
  }
  .brand-note {
    padding-left: 60px; padding-right: 22px;
    font-family: "Montserrat", Arial, sans-serif; font-weight: 600;
    font-size: 9.6px; line-height: 12.4px;
  }
</style>
</head>
<body>
<div class="page">
  <h1 class="section-title"><span class="num">6.</span>How does the Bedrock Yield Private Holdings<span class="line2">Scheme work?</span></h1>

  <div class="world-map" role="img" aria-label="Faint world map in the background"></div>

  <svg class="diagram" viewBox="0 0 848 1200" aria-hidden="true">
    <defs>
      <radialGradient id="disc" cx="40%" cy="35%" r="70%">
        <stop offset="0" stop-color="#ffffff"/>
        <stop offset="1" stop-color="#d6d8d8"/>
      </radialGradient>
    </defs>
    <g fill="none" stroke="var(--frame-green)" stroke-width="1.5">
      <polyline points="168,441 168,512 188,532 245,532"/>
      <line x1="424" y1="360" x2="424" y2="404"/>
      <polyline points="676,459 676,512 656,532 604,532"/>
      <polyline points="195,771 195,722 215,703 262,703"/>
      <polyline points="659,771 659,721 639,703 586,703"/>
      <circle cx="424" cy="605" r="137" stroke-width="2"/>
    </g>
    <g stroke="var(--ring-dark)" stroke-width="5" fill="url(#disc)">
      <circle cx="424" cy="605" r="85" stroke-width="7"/>
      <circle cx="424" cy="451" r="46"/>
      <circle cx="291" cy="532" r="46"/>
      <circle cx="557" cy="532" r="46"/>
      <circle cx="311" cy="703" r="46"/>
      <circle cx="537" cy="703" r="46"/>
    </g>
    <text x="424" y="617" text-anchor="middle" font-family="Montserrat, Arial, sans-serif" font-weight="900" font-size="76" fill="var(--accent-green)">5</text>
    <g font-family="Montserrat, Arial, sans-serif" font-weight="800" font-size="12.5" fill="#4f5553" text-anchor="middle">
      <text x="424" y="636">STEP</text>
      <text x="424" y="650">INVESTMENT</text>
      <text x="424" y="664">PROCESS</text>
    </g>
    <g fill="none" stroke="#5a5f5e" stroke-width="1.8" stroke-linecap="round" stroke-linejoin="round">
      <circle cx="285" cy="526" r="13"/>
      <line x1="294" y1="535" x2="308" y2="551" stroke-width="3"/>
      <circle cx="424" cy="433" r="9"/>
      <polyline points="419,433 423,437 430,429"/>
      <path d="M404 455 l10 -6 l10 4 l10 -4 l10 6 M410 457 l12 9 l6 -3 l5 3 l5 -6"/>
      <line x1="541" y1="512" x2="555" y2="528"/>
      <circle cx="560" cy="532" r="5"/>
      <rect x="546" y="542" width="14" height="4"/><rect x="546" y="547" width="14" height="4"/>
      <rect x="563" y="536" width="14" height="4"/><rect x="563" y="541" width="14" height="4"/><rect x="563" y="546" width="14" height="4"/>
      <line x1="540" y1="554" x2="582" y2="554"/>
      <circle cx="537" cy="705" r="19"/>
      <rect x="524" y="692" width="12" height="8" rx="2"/>
      <rect x="539" y="706" width="12" height="8" rx="2"/>
      <circle cx="520" cy="688" r="4"/><circle cx="555" cy="720" r="4"/>
      <rect x="300" y="685" width="22" height="30"/>
      <line x1="304" y1="691" x2="318" y2="691"/>
      <text x="311" y="708" text-anchor="middle" font-family="Montserrat, Arial, sans-serif" font-size="15" fill="#5a5f5e" stroke="none">$</text>
      <polyline points="287,701 296,701 293,698"/>
      <polyline points="335,701 326,701 329,698"/>
    </g>
  </svg>

  <section class="step-box step-identify">
    <h2>1. Identify</h2>
    <ul>
      <li>Stonebrook has a proven, ongoing acquisition strategy with supporting infrastructure that acquires producing oil and gas mineral/royalty assets on a weekly basis.</li>
      <li>Stonebrook holds these assets in its own portfolio for a limited period and transitions them to various partnerships or to individuals.</li>
    </ul>
  </section>

  <section class="step-box step-acquire">
    <h2>2. Acquire</h2>
    <ul>
      <li>Private Holdings investors acquire a diverse group of producing energy royalties with a $50,000 minimum investment.</li>
      <li>The portfolio will be adapted to the investment objectives of the investor.</li>
    </ul>
  </section>

  <section class="step-box step-reinvest">
    <h2>3. Reinvestment</h2>
    <ul>
      <li>Throughout the year and in alignment with the investor’s objectives, Stonebrook will reinvest the cash flow from the initial portfolio into more royalty interests to increase the investor’s asset base as well as their long-term cash flow.</li>
      <li>At some point, at the discretion of the owner/ investor, Stonebrook will stop the reinvestment plan and direct all monthly payments to go straight to the owner.</li>
    </ul>
  </section>

  <section class="step-box step-divest">
    <h2>5. Divestment</h2>
    <p>When/If the owner chooses to sell any or all their portfolio, Stonebrook will assist them in the divestment by:</p>
    <ul>
      <li>Providing the necessary data and documentation and advise them on various divestiture outlets.</li>
      <li>Set up the divestment for the seller with one or more outlets.</li>
      <li>Manage the sale process through funding.</li>
    </ul>
  </section>

  <section class="step-box step-manage">
    <h2>4. Manage</h2>
    <ul>
      <li>Stonebrook will manage the entire acquisition process from the legal documents, recording of title, notifying operators, notifying the taxing agencies, and transferring payments.</li>
      <li>Stonebrook’s affiliate royalty management company, Harlow Royalty Services, LLC, will provide monthly cash flow statements, quarterly investment statements, and year end statistics and tax statements.</li>
    </ul>
  </section>

  <footer class="brand-band">
    <div class="brand-name">STONEBROOK<br>MINERALS, LLC</div>
    <p class="brand-note">Nis que nobis nimolor apiduciat venihil iusam doloreiunt es ariat quasperunda qui cus magnate niet ipsum volore volectet, volorum qui occuptatqui odis renda simpor sinis dis Os iderit ipiste porendelest voloria tionseque porum fugiti quaes derspic ipicia abor ad quam, odigentur solut quo explitio quam, tem fugitae.</p>
  </footer>
</div>
</body>
</html>
```